Business cards to launch an education platform

Hi,
I am looking at having new business cards designed.
I am a startup, developing a web platform for schools and university, the education world. It's an online assessment system.
I would like a card that looks classy, and that is using the colors and the font of my logo.

I have attached:
1) my logo
2) A business card that I have designed quickly so you can have all the information required in the card, but I really don't like it.
3) The font that I am using (Lato Regular) to design my web platform
4) Some screenshots of my web platform so you can have a look at the style that I have.

Target Market(s)

Major market: Education system: Schools and university
Minor markets: Business in general

Industry/Entity Type

Business

Contact Information for Business Card

Lydia Marsh
Director

M: 0437 681 902
E: lydia.marsh@copperLeafSystems.com.au

Requirements
Must have
• The colors of my logo

```html
<!DOCTYPE html>
<html lang="en">
<head>
<meta charset="utf-8">
<title>Copper Leaf Systems – Business Card</title>
<link rel="stylesheet" href="https://fonts.googleapis.com/css2?family=Lato:wght@400;700&display=swap">
<style>
  :root {
    --page-bg: #e9ebee;
    --card-bg: #f7f7f7;
    --navy: #1f4e8c;
    --sky: #2bb2ea;
    --ink: #2c4f82;
  }
  * { box-sizing: border-box; margin: 0; padding: 0; }
  html, body {
    width: 1200px;
    height: 999px;
    overflow: hidden;
    background: var(--page-bg);
    font-family: "Lato", sans-serif;
  }
  .sheet {
    position: relative;
    width: 1200px;
    height: 999px;
  }
  .card {
    position: absolute;
    left: 250px;
    width: 700px;
    height: 410px;
    background: var(--card-bg);
    box-shadow: 0 6px 18px rgba(0,0,0,0.12);
    overflow: hidden;
  }
  .card--back { top: 60px; }
  .card--front { top: 530px; }

  .rule {
    position: absolute;
    height: 4px;
    background: var(--sky);
  }

  .brand {
    position: absolute;
    display: flex;
    align-items: center;
    gap: 14px;
  }
  .brand__mark {
    width: 54px;
    height: 54px;
    background: var(--navy);
    flex: none;
  }
  .brand__name {
    font-weight: 700;
    font-size: 26px;
    line-height: 1.05;
    color: var(--navy);
    letter-spacing: 0.5px;
  }

  /* back side */
  .card--back .rule--left  { left: 0; top: 203px; width: 215px; }
  .card--back .rule--right { left: 485px; top: 203px; width: 215px; }
  .card--back .brand { left: 230px; top: 178px; }

  /* front side */
  .card--front .rule--lead { left: 0; top: 178px; width: 40px; }
  .card--front .rule--main { left: 330px; top: 238px; width: 370px; }
  .card--front .brand { left: 55px; top: 152px; }

  .holder {
    position: absolute;
    right: 55px;
    top: 140px;
    text-align: right;
  }
  .holder__name {
    font-size: 40px;
    font-weight: 700;
    line-height: 1;
    letter-spacing: 0.5px;
    color: var(--navy);
  }
  .holder__name .surname { color: var(--sky); }
  .holder__role {
    font-size: 28px;
    font-weight: 400;
    color: var(--ink);
    margin-top: 4px;
  }

  .contact {
    position: absolute;
    right: 55px;
    top: 262px;
    text-align: right;
    color: var(--ink);
  }
  .contact__phone {
    font-size: 25px;
    display: flex;
    align-items: center;
    justify-content: flex-end;
    gap: 6px;
  }
  .contact__phone svg { width: 18px; height: 18px; }
  .contact__email {
    font-size: 19px;
    margin-top: 4px;
  }
</style>
</head>
<body>
<main class="sheet">

  <section class="card card--back" aria-label="Card back">
    <div class="rule rule--left"></div>
    <div class="brand">
      <div class="brand__mark"></div>
      <div class="brand__name">COPPER LEAF<br>Systems</div>
    </div>
    <div class="rule rule--right"></div>
  </section>

  <section class="card card--front" aria-label="Card front">
    <div class="rule rule--lead"></div>
    <div class="brand">
      <div class="brand__mark"></div>
      <div class="brand__name">COPPER LEAF<br>Systems</div>
    </div>

    <div class="holder">
      <div class="holder__name">LYDIA <span class="surname">MARSH</span></div>
      <div class="holder__role">Director</div>
    </div>

    <div class="rule rule--main"></div>

    <div class="contact">
      <div class="contact__phone">
        <svg viewBox="0 0 24 24" aria-hidden="true">
          <path fill="#2bb2ea" d="M6.6 10.8c1.4 2.8 3.8 5.1 6.6 6.6l2.2-2.2c.3-.3.7-.4 1-.2 1.1.4 2.3.6 3.6.6.6 0 1 .4 1 1V20c0 .6-.4 1-1 1C10.6 21 3 13.4 3 4c0-.6.4-1 1-1h3.5c.6 0 1 .4 1 1 0 1.3.2 2.5.6 3.6.1.3 0 .7-.2 1l-2.3 2.2z"/>
        </svg>
        <span>0437 681 902</span>
      </div>
      <div class="contact__email">lydia.marsh@copperLeafSystems.com.au</div>
    </div>
  </section>

</main>
</body>
</html>
```